Flyer/Poster design required for volunteer activities

We need a STRIKING A4 Poster/Flyer advertising our conservation volunteer program activities which are currently happening in the area. This poster is to advertise the program once people have arrived on the island or to locals. The program covers 5 months, May-September 2019 and is focused on conservation. I have attached the following:
- a flyer which was previously created (QMR Habitat Helpers 2019 sm)to advertise the program - would prefer it has a similar striking resemblance, but not essential
- A mock up document 'HHQMR On Island Poster_2019_v2' with text -Logos-Images

Target Market(s)

Everyone interested in Environmental Adventure/Hiking/Citizen Science

Industry/Entity Type

Tourism

Font styles to use
Sans Serif

Requirements
Must have
• -A travel conservation focus
• -Must use 'QMR-Background Image' as the background to the design
• -The info of where to get more information and the social media details must be prominent

```html
<!DOCTYPE html>
<html lang="en">
<head>
<meta charset="utf-8">
<title>QMR Habitat Helpers – May to September 2019</title>
<link rel="stylesheet" href="https://fonts.googleapis.com/css2?family=Oswald:wght@600&family=Source+Sans+3:wght@400;700&display=swap">
<style>
  :root {
    --page: #2a2a2a;
    --navy: #1f3a7a;
    --navy-deep: #1b3470;
    --sky-blue: #1e8ad0;
    --ink: #111418;
    --white: #ffffff;
  }
  * { box-sizing: border-box; margin: 0; padding: 0; }
  html, body {
    width: 1200px; height: 1200px; overflow: hidden;
    background: var(--page);
  }
  .poster {
    position: absolute; left: 182px; top: 13px;
    width: 836px; height: 1174px; overflow: hidden;
    font-family: "Source Sans 3", "Myriad Pro", sans-serif;
    color: var(--ink);
  }
  .backdrop {
    position: absolute; inset: 0;
    background:
      linear-gradient(180deg,
        #9fc2e6 0%, #eef3f8 8%, #ffffff 16%, #ffffff 26%,
        #f2f5f9 40%, #e4eaf1 55%, #eef2f6 68%, #cfdbe7 80%,
        #8fb8dc 86%, #5f8fb3 90%, #6f8d6a 95%, #4f6e58 100%);
  }
  .header-wash {
    position: absolute; left: 0; top: 0; width: 100%; height: 304px;
    background: linear-gradient(180deg, rgba(255,255,255,0) 0%, rgba(255,255,255,.85) 45%, #fff 100%);
  }
  .brand {
    position: absolute; left: 40px; top: 96px; width: 150px;
    display: flex; flex-direction: column; align-items: center; gap: 8px;
  }
  .brand-dot {
    width: 44px; height: 44px; border-radius: 50%;
    background: var(--navy);
  }
  .brand-name {
    font-weight: 700; font-size: 20px; line-height: 22px;
    color: var(--navy); text-align: center;
  }
  .title {
    position: absolute; left: 203px; top: 50px;
    font-family: "Oswald", "Bebas Neue", sans-serif; font-weight: 600;
    font-size: 58px; line-height: 58px; letter-spacing: -0.5px;
    color: var(--navy); text-transform: uppercase;
  }
  .dates {
    position: absolute; left: 198px; top: 177px; width: 520px; height: 64px;
    background: var(--sky-blue); color: var(--white);
    font-weight: 700; font-size: 48px; line-height: 64px; padding-left: 6px;
  }
  .tagline {
    position: absolute; left: 196px; top: 258px;
    font-weight: 700; font-size: 31px; line-height: 32px;
    color: var(--sky-blue); text-transform: uppercase;
  }
  .band {
    position: absolute; left: 0; top: 304px; width: 100%; height: 46px;
    background: var(--navy-deep); color: var(--white);
    font-weight: 700; font-size: 27px; line-height: 46px; text-align: center;
    text-transform: uppercase;
  }
  .schedule, .topics { position: absolute; list-style: none; }
  .schedule li, .topics li {
    position: absolute; font-weight: 700; font-size: 23px; line-height: 30px;
    white-space: nowrap;
  }
  .schedule { left: 30px; top: 0; }
  .schedule .month { text-transform: uppercase; display: block; }
  .topics { left: 518px; top: 0; }
  .topics li { text-transform: uppercase; }
  .divider {
    position: absolute; left: 440px; top: 374px; width: 1.5px; height: 490px;
    background: var(--navy);
  }
  .footer {
    position: absolute; left: 0; bottom: 0; width: 100%; height: 87px;
    background: var(--navy-deep); color: var(--white); text-align: center;
    padding-top: 12px;
  }
  .footer .info { font-size: 15.5px; line-height: 22px; }
  .footer .social { font-weight: 700; font-size: 18.5px; line-height: 24px; }
</style>
</head>
<body>
  <main class="poster">
    <div class="backdrop" role="img" aria-label="Background photo: cloudy sky over an island bay, with a hiker carrying a backpack looking out over green hills and the ocean"></div>
    <div class="header-wash"></div>

    <div class="brand">
      <span class="brand-dot"></span>
      <span class="brand-name">QMR Habitat Helpers</span>
    </div>

    <h1 class="title">QMR<br>Habitat Helpers</h1>
    <div class="dates">May – September 2019</div>
    <p class="tagline">Be involved in protecting paradise</p>

    <div class="band">Join the QMR Habitat Helpers program 2019</div>

    <ul class="schedule">
      <li style="top:374px"><span class="month">May 2019</span>Feature Week: 19th – 26th May</li>
      <li style="top:492px"><span class="month">June 2019</span>Feature Week:3rd- 9th June</li>
      <li style="top:610px"><span class="month">July 2019</span>Feature Week:21st – 28th July</li>
      <li style="top:728px"><span class="month">August 2019</span>Feature Week:11th-19th<br>August</li>
      <li style="top:874px"><span class="month">September 2019</span>Feature Week:1st-8th September</li>
    </ul>

    <div class="divider"></div>

    <ul class="topics">
      <li style="top:371px">Birds of QMR</li>
      <li style="top:499px">QMR<br>Marine Park</li>
      <li style="top:624px">Invasive species</li>
      <li style="top:753px">Amazing invertebrates</li>
      <li style="top:894px">Protecting paradise</li>
    </ul>

    <footer class="footer">
      <p class="info">See the QMR visitor centre for more information about the QMR Habitat Helpers program for 2019</p>
      <p class="social">FOLLOW US ! &nbsp;www.hhqmr-volunteers.org &nbsp;@hhqmr</p>
    </footer>
  </main>
</body>
</html>
```